Biker App Design
Zielgruppe
VeloMarn erstellt eine App für Biker mit der:
- Motorradfahrer andere Biker finden können um gemeinsam zu fahren
- Motorradfahrer ihre Strecke tracken können um Punkte zu sammeln
- Biker können mit diesen Punkten Ränge aufsteigen 'Masterbiker, Anfänger, GuruFahrer, etc.', es soll eine Art 'Erfahrungsleiste' angezeigt werden
- Diese Punkte können gegen Gutscheine/Wertsachen eingelöst werden
- Es gibt Nachrichten (Art Blogeinträge) genau zu diesen Themen
Aufgabenstellung
Modernes Design
Reduziert
Es werden folgende Screens benötigt:
Startbild
Start - Dateneintragen:
Um den Fahrer besser mit anderen Fahren zu verknüpfen muss er folgende informationen angeben:
- Welche Art Motorrad fährt er? Sport, Vintage, Cross
- Männlich/Weiblich/Divers
- Geburtsjahr
- PLZ des Heimatorts
- Nickname
Startscreen um andere Biker zu suchen und damit eine Tour zu starten
- Hier sollte ein 'Map' Bild mit einem Kreis für den Umkreis dargestellt werden + Pins mit Personenbilder , welche
Personen in der Nähe sind und auch fahren möchten
- Hier sollte stehen, wieviel Punkte er noch benötigt um den nächsten Gutschein freizuschalten
Screen zum Start des Trackens
Screen während dem Tracken mit Pause/Stop-Option
Screen mit einem Überblick der neuen Blogeinträge
Screen beim beenden des Trackens (Strecke speichern, Bild hinzufügen, Freunde informieren ich bin angekommen)
Screen Profilseite, Bild des Bikers + Bike + Erfahrungspunkte + gesammelte Errungenschaften z.B. 'Mit 3 Freunden mehr als 1000km gefahren'
Screen Bestenliste, anhand der Punkte
Es sollen Dateiformate verwendet werden, die gut wiederverwendet werden können. Es sollen sich Bausteine aus diesen Design wiederverwenden lassen können.
Wir benötigen eine APP mit einem User-Dashboards (Life-Account) in dem Finanz, Karriere und Gesundheitsthemen erkennbar sein sollen. Look and Feel soll seriös, schnörkelos und modern sein.
Das Design soll simpel sein. Also Verwendung von wenigen, dezenten Farben (Schattierungen / Blendeffekte erlaubt) und san-serife / simple schrift. Ich würde es mit progressiv, technisch, eher jugendlich, eher offen/frisch, modern, eher prägnant, clean, urban, eher freundschaftlich, schlicht, ehe..
hallo, wir brauchen das design für eine startseite. thema taxi app alle weiteren infos siehe anhang pdf eilauftrag - sofort kauf möglich danke
Unter Flickhafen.de kann das aktuelle Design angeschaut werden. Die Farbe sollten übernommen werden. Über die Startseite kann der Kunde sein Gerät, Service sowie seine Adresse eingeben. Auf der Vergleichsseite bekommt der Kunde die Übersicht welche Reparaturwerkstätten es gibt, zu welch..
Vorweg: Dem Auftrag folgen weitere Teilaufträge an den Gewinner, natürlich gegen Bezahlung. Für die bereits programmierte Webapplikation "tocks" wird ein Design benötigt. Tocks ähnelt den bereits bestehenden Zeiterfassungssystemen, soll sich aber anhand von Einfachheit, Speditivität und..

```html
<!DOCTYPE html>
<html lang="en">
<head>
<meta charset="utf-8">
<title>VeloMarn – Biker App Screens</title>
<link rel="stylesheet" href="https://fonts.googleapis.com/css2?family=Montserrat:wght@400;500;600;700;800&family=Saira:wght@600;700&display=swap">
<style>
:root{
  --stage:#1f1f20;
  --screen:#2c2d2f;
  --panel:#35363a;
  --panel-light:#3f4044;
  --bar:#26272a;
  --green:#3bc41d;
  --red:#e3201f;
  --text:#ffffff;
  --muted:#8d8e92;
  --faint:#55565a;
  --map-a:#2a2b2e;
  --map-b:#3a3b3f;
}
*{box-sizing:border-box;margin:0;padding:0}
html,body{width:941px;height:1200px;overflow:hidden;background:var(--stage);font-family:"Montserrat",sans-serif;color:var(--text)}
.board{position:relative;width:941px;height:1200px}
.screen{position:absolute;width:271px;height:360px;background:var(--screen);border-radius:10px;overflow:hidden;box-shadow:0 14px 30px rgba(0,0,0,.45)}
.c1{left:28px}.c2{left:335px}.c3{left:642px}
.r1{top:30px}.r2{top:420px}.r3{top:810px}

.status{height:16px;display:flex;justify-content:flex-end;align-items:center;gap:4px;padding:0 10px;font-size:7px;font-weight:600;background:var(--bar)}
.appbar{height:24px;display:flex;align-items:center;justify-content:space-between;padding:0 10px;background:var(--bar)}
.appbar .tools{display:flex;gap:9px}
.icon{width:10px;height:10px;stroke:var(--muted);fill:none;stroke-width:1.4}
.nav{position:absolute;left:0;right:0;bottom:0;height:30px;background:var(--bar);display:flex;justify-content:space-around;align-items:center}
.nav .icon{width:12px;height:12px}
.nav .on{stroke:var(--red)}
.nav .on-green{stroke:var(--green)}

/* onboarding */
.onboard-head{height:24px;display:flex;align-items:center;padding:0 10px;background:var(--bar);position:relative}
.brand{position:absolute;left:0;right:0;text-align:center;font-size:9px;font-weight:700;color:var(--red)}
.hero{position:absolute;left:0;right:0;top:40px;bottom:0;background:linear-gradient(160deg,#2b3a4e 0%,#27303b 45%,#3a3c40 100%)}
.form{position:absolute;left:0;right:0;top:40px;bottom:0;padding:12px 16px}
.form h1{font-size:12px;font-weight:500;text-align:center;margin-bottom:12px}
.field{margin-bottom:9px}
.field label{display:block;font-size:6px;color:#c9cbd0}
.field .value{font-size:8.5px;padding:2px 0 3px;border-bottom:1px solid rgba(255,255,255,.35);display:flex;justify-content:space-between}
.dots{letter-spacing:4px;font-weight:700}
.segment{display:flex;margin:3px 0 9px}
.segment span{flex:1;font-size:8px;padding:4px 0;text-align:center;color:#d5d6da}
.segment .sel{background:var(--red);color:#fff;transform:skewX(-14deg)}
.segment .sel b{display:inline-block;transform:skewX(14deg);font-weight:500}
.cta{display:flex;justify-content:center;align-items:center;height:22px;background:var(--red);font-size:7px;font-weight:700;transform:skewX(-14deg);margin:12px 6px 0;letter-spacing:.3px}
.cta b{transform:skewX(14deg);font-weight:700}
.avatar{border-radius:50%;background:radial-gradient(circle at 40% 35%,#7f9ab8,#2f3e52);flex:none}
.center{text-align:center}
.small{font-size:6.5px;color:#d0d1d5}

/* profile */
.profile-top{display:flex;gap:9px;padding:8px 10px 6px}
.profile-top h2{font-size:11px;font-weight:700}
.profile-top .loc{font-size:5.5px;color:var(--muted);margin:1px 0 3px}
.profile-top p{font-size:5.5px;color:#b7b8bc;line-height:1.35}
.bike-bar{display:flex;height:16px;font-size:6.5px;font-weight:600;margin:0 10px}
.bike-bar .notch{width:16px;background:var(--green);transform:skewX(-20deg)}
.bike-bar .name{flex:1;background:var(--panel);display:flex;align-items:center;padding-left:10px}
.bike-bar .edit{width:70px;background:var(--panel-light);display:flex;align-items:center;justify-content:center;font-weight:500}
.rank{display:flex;justify-content:space-between;align-items:flex-end;padding:8px 16px 2px}
.rank h3{font-size:8px;font-weight:700}
.rank .pts{font-family:"Saira",sans-serif;color:var(--green);font-size:11px;line-height:1;text-align:right}
.rank .pts small{display:block;font-size:5px;color:var(--muted);font-family:"Montserrat",sans-serif}
.xp{display:flex;gap:3px;padding:0 16px}
.xp span{width:28px;height:3px;background:var(--red);transform:skewX(-20deg)}
.xp span.off{background:var(--faint)}
.xp-label{font-size:4.5px;color:var(--muted);padding:2px 16px 0}
.buy{font-size:6px;font-weight:700;text-align:center;margin:3px 0 6px}
.awards{display:flex;justify-content:space-around;padding:0 16px}
.award{width:60px;text-align:center;font-size:4.5px;color:#c3c4c8;line-height:1.3}
.award svg{width:11px;height:11px;stroke:var(--green);fill:none;stroke-width:1.3;display:block;margin:0 auto 3px}
.section-label{font-size:6px;color:var(--muted);text-align:center;margin:8px 0 4px}
.drive{display:flex;margin:0 10px;height:50px;background:var(--panel)}
.drive .thumb{width:60px;background:linear-gradient(135deg,var(--map-b),var(--map-a))}
.drive .info{flex:1;padding:5px 8px}
.drive h4{font-size:7px;font-weight:700}
.drive .date{font-size:4.5px;color:var(--muted)}
.drive .stats{display:flex;gap:12px;margin-top:8px}
.stat small{display:block;font-size:4.5px;color:var(--muted)}
.stat b{font-size:7px;font-weight:700}
.drive-next{font-size:7px;font-weight:700;padding:4px 0 0 80px}

/* tracking */
.compass{height:86px;position:relative}
.compass svg{position:absolute;left:0;top:0}
.metric{position:relative;height:27px;margin:3px 0;display:flex;align-items:center}
.tag{position:absolute;background:var(--green);font-size:5.5px;font-weight:700;padding:3px 10px 3px 8px;transform:skewX(-18deg)}
.tag b{display:inline-block;transform:skewX(18deg)}
.metric .big{font-family:"Saira",sans-serif;font-size:15px;position:absolute}
.metric .label{position:absolute;font-size:5.5px;font-weight:700}
.metric .ghost{position:absolute;font-family:"Saira",sans-serif;font-size:15px;color:rgba(255,255,255,.05);left:40px}
.metric.dark{background:var(--panel)}
.track-actions{position:absolute;left:0;right:0;bottom:38px;height:24px;display:flex}
.btn{display:flex;align-items:center;justify-content:center;gap:5px;font-size:7px;font-weight:700}
.btn svg{width:9px;height:9px;stroke:#fff;fill:none;stroke-width:1.5}
.btn-start{flex:0 0 70%;background:var(--green);transform:skewX(-14deg);margin-left:-6px}
.btn-start span,.btn-stop span{transform:skewX(14deg);display:flex;gap:5px;align-items:center}
.btn-pause{flex:1;background:var(--bar)}
.btn-stop{flex:1;background:var(--red);transform:skewX(-14deg);margin-right:-6px}
.btn-idle{flex:1;background:var(--bar)}

/* leaderboard */
.search{margin:6px 14px 6px;height:16px;display:flex;align-items:center;gap:5px;padding-left:6px;font-size:6px;color:var(--faint)}
.leader{display:flex;align-items:center;height:30px;padding-right:10px}
.leader .pos{width:44px;height:16px;font-family:"Saira",sans-serif;font-size:10px;display:flex;align-items:center;justify-content:center;color:#d6d7db}
.leader .pos.top{background:var(--green);color:#fff;transform:skewX(-16deg)}
.leader .pos.top b{transform:skewX(16deg);font-weight:700}
.leader .avatar{width:18px;height:18px;margin:0 7px 0 8px}
.leader h5{font-size:6.5px;font-weight:700}
.leader p{font-size:4.5px;color:var(--muted);line-height:1.3}

/* map */
.map{position:absolute;left:0;right:0;top:40px;bottom:30px;background:radial-gradient(ellipse at 55% 45%,var(--map-b),var(--map-a) 70%)}
.pin{position:absolute;width:16px;height:20px}
.map-user{position:absolute;left:0;right:0;bottom:30px;height:28px;background:var(--bar);display:flex;align-items:center}
.map-user .avatar{width:18px;height:18px;margin:0 6px 0 10px}
.map-user h5{font-size:6.5px;font-weight:700}
.map-user p{font-size:4.5px;color:var(--muted)}
.join{margin-left:auto;width:76px;height:100%;background:var(--green);display:flex;align-items:center;justify-content:center;font-size:7px;font-weight:700;transform:skewX(-14deg);margin-right:-6px}
.join span{transform:skewX(14deg)}

/* notes */
.note{padding:7px 12px 4px}
.note-head{display:flex;align-items:center;gap:6px}
.note-head .avatar{width:16px;height:16px}
.note-head h5{font-size:6.5px;font-weight:700}
.note-head small{display:block;font-size:4.5px;color:var(--muted);font-weight:400}
.note-head .time{margin-left:auto;font-size:4.5px;color:var(--muted)}
.note-head .time.new{color:var(--red)}
.note p{font-size:5px;color:#b9babe;line-height:1.35;margin-top:4px}
.write{position:absolute;left:30px;right:40px;bottom:38px;height:20px;background:var(--green);transform:skewX(-14deg);display:flex;align-items:center;justify-content:center;font-size:6.5px;font-weight:700}
.write span{transform:skewX(14deg)}
</style>
</head>
<body>
<div class="board">

<svg width="0" height="0" style="position:absolute">
  <defs>
    <symbol id="i-menu" viewBox="0 0 12 12"><path d="M1 3h10M1 6h10M1 9h10"/></symbol>
    <symbol id="i-search" viewBox="0 0 12 12"><circle cx="5" cy="5" r="3.5"/><path d="M7.6 7.6L11 11"/></symbol>
    <symbol id="i-bell" viewBox="0 0 12 12"><path d="M3 8.5V5.5a3 3 0 016 0v3l1 1H2zM5 10.5h2"/></symbol>
    <symbol id="i-gear" viewBox="0 0 12 12"><circle cx="6" cy="6" r="2"/><circle cx="6" cy="6" r="4.5" stroke-dasharray="2 1.5"/></symbol>
    <symbol id="i-map" viewBox="0 0 12 12"><path d="M1 3l3-1.5 4 1.5 3-1.5v8L8 11 4 9.5 1 11zM4 1.5v8M8 3v8"/></symbol>
    <symbol id="i-flag" viewBox="0 0 12 12"><path d="M3 11V1.5h6.5l-1.5 2.5 1.5 2.5H3"/></symbol>
    <symbol id="i-ring" viewBox="0 0 12 12"><circle cx="6" cy="6" r="4.5"/></symbol>
    <symbol id="i-stack" viewBox="0 0 12 12"><rect x="1.5" y="3.5" width="7" height="7" rx="1"/><path d="M4 3.5V1.5h6.5V8H8.5"/></symbol>
    <symbol id="i-user" viewBox="0 0 12 12"><circle cx="6" cy="4" r="2.5"/><path d="M1.5 11c.5-2.5 2.3-3.5 4.5-3.5s4 1 4.5 3.5"/></symbol>
    <symbol id="i-back" viewBox="0 0 12 12"><path d="M11 6H1.5M5 2.5L1.5 6 5 9.5"/></symbol>
    <symbol id="i-star" viewBox="0 0 12 12"><path d="M6 1l1.5 3.2 3.5.4-2.6 2.4.7 3.5L6 8.8 2.9 10.5l.7-3.5L1 4.6l3.5-.4z"/></symbol>
    <symbol id="i-signal" viewBox="0 0 24 8"><path d="M0 1h7L3.5 6z M9 7l4-6v6z M16 1h4v6h-4z" fill="#fff" stroke="none"/></symbol>
    <symbol id="i-pin" viewBox="0 0 16 20"><path d="M8 19C3 13 1 10 1 7a7 7 0 0114 0c0 3-2 6-7 12z" fill="#2c3a2c" stroke="#3bc41d" stroke-width="1.6"/><circle cx="8" cy="7" r="4" fill="#5f6b78" stroke="none"/></symbol>
    <symbol id="i-pin-red" viewBox="0 0 16 20"><path d="M8 19C3 13 1 10 1 7a7 7 0 0114 0c0 3-2 6-7 12z" fill="#3a2626" stroke="#e3201f" stroke-width="1.6"/><circle cx="8" cy="7" r="4" fill="#5f6b78" stroke="none"/></symbol>
  </defs>
</svg>

<!-- 1 · Sign up -->
<section class="screen c1 r1" aria-label="Sign up screen">
  <div class="status"><svg width="22" height="7"><use href="#i-signal"/></svg>12:30</div>
  <div class="onboard-head"><svg class="icon"><use href="#i-back"/></svg><span class="brand">VeloMarn</span></div>
  <div class="hero" role="img" aria-label="Photo of a rider leaning a sport motorcycle into a curve"></div>
  <div class="form">
    <h1>Sign up</h1>
    <div class="field"><label>Email address</label><div class="value">jondarrow789@velomail.app</div></div>
    <div class="field"><label>User name</label><div class="value">Jon Darrow</div></div>
    <div class="field"><label>Gender</label></div>
    <div class="segment" style="margin-top:-6px"><span class="sel"><b>Male</b></span><span>Female</span><span>Diverse</span></div>
    <div class="field"><label>Year of birth</label><div class="value">1996<span>⌄</span></div></div>
    <div class="field"><label>Password</label><div class="value dots">•••••••••</div></div>
    <div class="field"><label>Confirm password</label><div class="value dots">•••••••••</div></div>
    <div class="cta"><b>SIGN UP &nbsp;›</b></div>
  </div>
</section>

<!-- 2 · Profile details -->
<section class="screen c2 r1" aria-label="Profile details screen">
  <div class="status"><svg width="22" height="7"><use href="#i-signal"/></svg>12:30</div>
  <div class="onboard-head"><svg class="icon"><use href="#i-back"/></svg><span class="brand">VeloMarn</span></div>
  <div class="hero" role="img" aria-label="Photo of a rider on a sport motorcycle on a race track"></div>
  <div class="form">
    <h1 style="margin-top:6px">Few more informations</h1>
    <div class="avatar" role="img" aria-label="Profile photo of the rider" style="width:46px;height:46px;margin:0 auto 8px"></div>
    <p class="small center" style="margin-bottom:14px">Change profile picture</p>
    <p class="small center">What kind of motorcycle does he drive?</p>
    <div class="segment"><span class="sel"><b>Sport</b></span><span>Vintage</span><span>Cross</span></div>
    <div class="field"><label>Home ZIP CODE</label><div class="value">10000</div></div>
    <div class="cta" style="margin-top:22px"><b>CREATE PROFIL &nbsp;›</b></div>
  </div>
</section>

<!-- 3 · Profile -->
<section class="screen c3 r1" aria-label="Profile screen">
  <div class="status"><svg width="22" height="7"><use href="#i-signal"/></svg>12:30</div>
  <div class="appbar"><svg class="icon"><use href="#i-menu"/></svg><div class="tools"><svg class="icon"><use href="#i-search"/></svg><svg class="icon"><use href="#i-bell"/></svg><svg class="icon"><use href="#i-gear"/></svg></div></div>
  <div class="profile-top">
    <div class="avatar" role="img" aria-label="Profile photo of Jon Darrow on his motorcycle" style="width:40px;height:40px"></div>
    <div>
      <h2>Jon Darrow</h2>
      <div class="loc">Harlow, Northvale</div>
      <p>"Lorem ipsum dolor sit amet, consectetur adipiscing elit, sed do eiusmod tempor incididunt ut labore et dolore magna aliqua. Ut enim ad minim veniam."</p>
    </div>
  </div>
  <div class="bike-bar"><div class="notch"></div><div class="name">Kestrel KR 1000</div><div class="edit">Edit bike</div></div>
  <div class="rank"><h3>Guru Driver</h3><div class="pts">1892<small>pts</small></div></div>
  <div class="xp"><span></span><span></span><span class="off"></span><span class="off"></span><span class="off"></span></div>
  <div class="xp-label">Experience level</div>
  <div class="buy">Buy more!</div>
  <div class="awards">
    <div class="award"><svg><use href="#i-star"/></svg>With 3 friends drove more than 1000km</div>
    <div class="award"><svg><use href="#i-star"/></svg>7 centuries</div>
    <div class="award"><svg><use href="#i-star"/></svg>3 years on wheels</div>
  </div>
  <div class="section-label">Drives</div>
  <div class="drive">
    <div class="thumb" role="img" aria-label="Map thumbnail of the drive route"></div>
    <div class="info">
      <h4>Harlow - Fenwick Creek</h4>
      <div class="date">24.12.2019</div>
      <div class="stats">
        <div class="stat"><small>Start at</small><b>14:43</b></div>
        <div class="stat"><small>End at</small><b>14:43</b></div>
        <div class="stat"><small>Distance</small><b>464.2km</b></div>
      </div>
    </div>
  </div>
  <div class="drive-next">Ashford - Kell Island</div>
  <nav class="nav"><svg class="icon"><use href="#i-map"/></svg><svg class="icon"><use href="#i-flag"/></svg><svg class="icon"><use href="#i-ring"/></svg><svg class="icon"><use href="#i-stack"/></svg><svg class="icon on"><use href="#i-user"/></svg></nav>
</section>

<!-- 4 · Tracking ready -->
<section class="screen c1 r2" aria-label="Start tracking screen">
  <div class="status"><svg width="22" height="7"><use href="#i-signal"/></svg>12:30</div>
  <div class="appbar"><svg class="icon"><use href="#i-menu"/></svg><div class="tools"><svg class="icon"><use href="#i-search"/></svg><svg class="icon"><use href="#i-bell"/></svg><svg class="icon"><use href="#i-gear"/></svg></div></div>
  <div class="compass">
    <svg width="271" height="86" viewBox="0 0 271 86">
      <path d="M40 70 Q135 -5 231 70" fill="none" stroke="#6a6b6f" stroke-width="2"/>
      <text x="135" y="18" fill="#e3201f" font-family="Montserrat" font-weight="700" font-size="9" text-anchor="middle">N</text>
      <text x="34" y="44" fill="#8d8e92" font-family="Montserrat" font-size="6">W</text>
      <text x="232" y="44" fill="#8d8e92" font-family="Montserrat" font-size="6">E</text>
      <path d="M130 40 L140 34 L143 48 Z" fill="#fff"/>
      <text x="136" y="62" fill="#3bc41d" font-family="Montserrat" font-weight="600" font-size="6" text-anchor="middle">278°</text>
    </svg>
  </div>
  <div class="metric dark"><span class="tag" style="left:-4px"><b>hh:mm:ss</b></span><span class="big" style="left:62px">00:00:00</span><span class="label" style="right:12px">Recording Time</span></div>
  <div class="metric"><span class="label" style="left:14px">Distance</span><span class="ghost">Distance</span><span class="big" style="right:46px">0.0</span><span class="tag" style="right:-4px"><b>km</b></span></div>
  <div class="metric dark"><span class="tag" style="left:-4px"><b>km/h</b></span><span class="big" style="left:50px">0.0</span><span class="ghost" style="left:110px">Avrg</span><span class="label" style="right:12px">Avrage speed</span></div>
  <div class="metric"><span class="label" style="left:14px">Altitude</span><span class="ghost">Altitude</span><span class="big" style="right:46px">0</span><span class="tag" style="right:-4px"><b>m</b></span></div>
  <div class="track-actions"><div class="btn btn-start"><span><svg><use href="#i-ring"/></svg>Start</span></div><div class="btn btn-idle"></div></div>
  <nav class="nav"><svg class="icon"><use href="#i-map"/></svg><svg class="icon"><use href="#i-flag"/></svg><svg class="icon on-green" style="width:16px;height:16px"><use href="#i-ring"/></svg><svg class="icon"><use href="#i-stack"/></svg><svg class="icon"><use href="#i-user"/></svg></nav>
</section>

<!-- 5 · Tracking running -->
<section class="screen c2 r2" aria-label="Tracking in progress screen">
  <div class="status"><svg width="22" height="7"><use href="#i-signal"/></svg>12:30</div>
  <div class="appbar"><svg class="icon"><use href="#i-menu"/></svg><div class="tools"><svg class="icon"><use href="#i-search"/></svg><svg class="icon"><use href="#i-bell"/></svg><svg class="icon"><use href="#i-gear"/></svg></div></div>
  <div class="compass">
    <svg width="271" height="86" viewBox="0 0 271 86">
      <path d="M40 70 Q135 -5 231 70" fill="none" stroke="#6a6b6f" stroke-width="2"/>
      <text x="135" y="18" fill="#e3201f" font-family="Montserrat" font-weight="700" font-size="9" text-anchor="middle">N</text>
      <text x="34" y="44" fill="#8d8e92" font-family="Montserrat" font-size="6">W</text>
      <text x="232" y="44" fill="#8d8e92" font-family="Montserrat" font-size="6">E</text>
      <path d="M130 40 L140 34 L143 48 Z" fill="#fff"/>
      <text x="136" y="62" fill="#3bc41d" font-family="Montserrat" font-weight="600" font-size="6" text-anchor="middle">278°</text>
    </svg>
  </div>
  <div class="metric dark"><span class="tag" style="left:-4px"><b>hh:mm:ss</b></span><span class="big" style="left:62px">00:59:34</span><span class="label" style="right:12px">Recording Time</span></div>
  <div class="metric"><span class="label" style="left:14px">Distance</span><span class="ghost">Distance</span><span class="big" style="right:46px">165.3</span><span class="tag" style="right:-4px"><b>km</b></span></div>
  <div class="metric dark"><span class="tag" style="left:-4px"><b>km/h</b></span><span class="big" style="left:50px">121.3</span><span class="ghost" style="left:110px">Avrg</span><span class="label" style="right:12px">Avrage speed</span></div>
  <div class="metric"><span class="label" style="left:14px">Altitude</span><span class="ghost">Altitude</span><span class="big" style="right:46px">1720</span><span class="tag" style="right:-4px"><b>m</b></span></div>
  <div class="track-actions"><div class="btn btn-pause"><b>||</b>&nbsp;Pause</div><div class="btn btn-stop"><span><svg><rect x="1" y="1" width="7" height="7" rx="1.5"/></svg>Stop</span></div></div>
  <nav class="nav"><svg class="icon"><use href="#i-map"/></svg><svg class="icon"><use href="#i-flag"/></svg><svg class="icon on" style="width:16px;height:16px"><use href="#i-ring"/></svg><svg class="icon"><use href="#i-stack"/></svg><svg class="icon"><use href="#i-user"/></svg></nav>
</section>

<!-- 6 · Leaderboard -->
<section class="screen c3 r2" aria-label="Leaderboard screen">
  <div class="status"><svg width="22" height="7"><use href="#i-signal"/></svg>12:30</div>
  <div class="appbar"><svg class="icon"><use href="#i-menu"/></svg><div class="tools"><svg class="icon"><use href="#i-search"/></svg><svg class="icon"><use href="#i-bell"/></svg><svg class="icon"><use href="#i-gear"/></svg></div></div>
  <div class="search"><svg class="icon" style="stroke:var(--faint)"><use href="#i-search"/></svg>Search Leaderboard</div>
  <div class="leader"><span class="pos top"><b>1st</b></span><div class="avatar" role="img" aria-label="Photo of Sem Lodvar"></div><div><h5>Sem Lodvar</h5><p>Sport<br>45 km away from you</p></div></div>
  <div class="leader"><span class="pos top"><b>2nd</b></span><div class="avatar" role="img" aria-label="Photo of Rickard Brolle"></div><div><h5>Rickard Brolle</h5><p>Sport<br>45 km away from you</p></div></div>
  <div class="leader"><span class="pos top"><b>3rd</b></span><div class="avatar" role="img" aria-label="Photo of Robyn Dellar"></div><div><h5>Robyn Dellar</h5><p>Sport<br>45 km away from you</p></div></div>
  <div class="leader"><span class="pos">4th</span><div class="avatar" role="img" aria-label="Photo of Rolf Sandoval"></div><div><h5>Rolf Sandoval</h5><p>Sport<br>45 km away from you</p></div></div>
  <div class="leader"><span class="pos">5th</span><div class="avatar" role="img" aria-label="Photo of Marek Alvin"></div><div><h5>Marek Alvin</h5><p>Sport<br>45 km away from you</p></div></div>
  <div class="leader"><span class="pos">6th</span><div class="avatar" role="img" aria-label="Photo of Serik Molvan"></div><div><h5>Serik Molvan</h5><p>Sport<br>45 km away from you</p></div></div>
  <div class="leader"><span class="pos">7th</span><div class="avatar" role="img" aria-label="Photo of Mark Van Berlingen"></div><div><h5>Mark Van Berlingen</h5><p>Sport<br>45 km away from you</p></div></div>
  <div class="leader"><span class="pos">8th</span><div class="avatar" role="img" aria-label="Photo of Sofie Arnvik"></div><div><h5>Sofie Arnvik</h5><p>Sport</p></div></div>
  <nav class="nav"><svg class="icon"><use href="#i-map"/></svg><svg class="icon on"><use href="#i-flag"/></svg><svg class="icon"><use href="#i-ring"/></svg><svg class="icon"><use href="#i-stack"/></svg><svg class="icon"><use href="#i-user"/></svg></nav>
</section>

<!-- 7 · Map of nearby riders -->
<section class="screen c1 r3" aria-label="Nearby riders map screen">
  <div class="status"><svg width="22" height="7"><use href="#i-signal"/></svg>12:30</div>
  <div class="appbar"><svg class="icon"><use href="#i-menu"/></svg><div class="tools"><svg class="icon"><use href="#i-search"/></svg><svg class="icon"><use href="#i-bell"/></svg><svg class="icon"><use href="#i-gear"/></svg></div></div>
  <div class="map" role="img" aria-label="Dark street map of a coastal city and its suburbs"></div>
  <svg class="pin" style="left:110px;top:70px"><use href="#i-pin"/></svg>
  <svg class="pin" style="left:90px;top:120px"><use href="#i-pin"/></svg>
  <svg class="pin" style="left:150px;top:135px"><use href="#i-pin"/></svg>
  <svg class="pin" style="left:166px;top:140px"><use href="#i-pin"/></svg>
  <svg class="pin" style="left:120px;top:230px"><use href="#i-pin"/></svg>
  <svg class="pin" style="left:190px;top:225px"><use href="#i-pin"/></svg>
  <nav class="nav"><svg class="icon on"><use href="#i-map"/></svg><svg class="icon"><use href="#i-flag"/></svg><svg class="icon"><use href="#i-ring"/></svg><svg class="icon"><use href="#i-stack"/></svg><svg class="icon"><use href="#i-user"/></svg></nav>
</section>

<!-- 8 · Map with selected rider -->
<section class="screen c2 r3" aria-label="Join a rider screen">
  <div class="status"><svg width="22" height="7"><use href="#i-signal"/></svg>12:30</div>
  <div class="appbar"><svg class="icon"><use href="#i-menu"/></svg><div class="tools"><svg class="icon"><use href="#i-search"/></svg><svg class="icon"><use href="#i-bell"/></svg><svg class="icon"><use href="#i-gear"/></svg></div></div>
  <div class="map" role="img" aria-label="Dark street map of a coastal city and its suburbs"></div>
  <svg class="pin" style="left:70px;top:80px"><use href="#i-pin-red"/></svg>
  <svg class="pin" style="left:130px;top:65px"><use href="#i-pin"/></svg>
  <svg class="pin" style="left:120px;top:120px"><use href="#i-pin"/></svg>
  <svg class="pin" style="left:180px;top:130px"><use href="#i-pin"/></svg>
  <svg class="pin" style="left:135px;top:220px"><use href="#i-pin"/></svg>
  <svg class="pin" style="left:205px;top:215px"><use href="#i-pin"/></svg>
  <div class="map-user">
    <div class="avatar" role="img" aria-label="Photo of Sem Lodvar"></div>
    <div><h5>Sem Lodvar</h5><p>Sport · 45 km away from you</p></div>
    <div class="join"><span>Join</span></div>
  </div>
  <nav class="nav"><svg class="icon on"><use href="#i-map"/></svg><svg class="icon"><use href="#i-flag"/></svg><svg class="icon"><use href="#i-ring"/></svg><svg class="icon"><use href="#i-stack"/></svg><svg class="icon"><use href="#i-user"/></svg></nav>
</section>

<!-- 9 · Notes feed -->
<section class="screen c3 r3" aria-label="Notes feed screen">
  <div class="status"><svg width="22" height="7"><use href="#i-signal"/></svg>12:30</div>
  <div class="appbar"><svg class="icon"><use href="#i-menu"/></svg><div class="tools"><svg class="icon"><use href="#i-search"/></svg><svg class="icon"><use href="#i-bell"/></svg><svg class="icon"><use href="#i-gear"/></svg></div></div>
  <article class="note"><div class="note-head"><div class="avatar" role="img" aria-label="Photo of Sem Lodvar"></div><h5>Sem Lodvar<small>Sport</small></h5><span class="time new">Just now</span></div>
    <p>Lorem ipsum dolor sit amet, consectetur adipisicing elit, sed do eiusmod tempor incididunt ut labore et dolore magna aliqua. Ut enim ad minim veniam, quis nostrud exercitation ullamco laboris nisi ut aliquip ex ea commodo consequat.</p></article>
  <article class="note"><div class="note-head"><div class="avatar" role="img" aria-label="Photo of Rickard Brolle"></div><h5>Rickard Brolle<small>Sport</small></h5><span class="time">5 min ago</span></div>
    <p>Lorem ipsum dolor sit amet, consectetur adipisicing elit, sed do eiusmod tempor incididunt ut labore et dolore magna aliqua. Ut enim ad minim veniam, quis nostrud exercitation ullamco laboris.</p></article>
  <article class="note"><div class="note-head"><div class="avatar" role="img" aria-label="Photo of Robyn Dellar"></div><h5>Robyn Dellar<small>Sport</small></h5><span class="time">51 min ago</span></div>
    <p>Lorem ipsum dolor sit amet, consectetur adipisicing elit, sed do eiusmod tempor incididunt ut labore et dolore magna aliqua.</p></article>
  <article class="note"><div class="note-head"><div class="avatar" role="img" aria-label="Photo of Rolf Sandoval"></div><h5>Rolf Sandoval<small>Sport</small></h5><span class="time">1 day ago</span></div></article>
  <div class="write"><span>Write note</span></div>
  <nav class="nav"><svg class="icon"><use href="#i-map"/></svg><svg class="icon"><use href="#i-flag"/></svg><svg class="icon"><use href="#i-ring"/></svg><svg class="icon on"><use href="#i-stack"/></svg><svg class="icon"><use href="#i-user"/></svg></nav>
</section>

</div>
</body>
</html>
```